Consulting company needs Business Cards - rough concept provided

I'm looking for someone to take our business card idea and make is slick and polished - to communicate our high-end, sophisticated, serious consulting business. We have a rough layout we did in-house. We are open to ideas on repo-ing elements, adjusting sizes, typefaces etc... within the general concept we've already come up with. We want it to be super-clean and sophisticated. We want to keep the white backgrounds, and blue brand colors. Our goal is to print with painted blue edges on thick cardstock. Thank you!!

```html
<!DOCTYPE html>
<html lang="en">
<head>
<meta charset="utf-8">
<title>Brighthold Stationery</title>
<link href="https://fonts.googleapis.com/css2?family=Montserrat:wght@700&family=Source+Sans+3:wght@400;600&display=swap" rel="stylesheet">
<style>
  :root {
    --brand-blue: #0a72c0;
    --paper: #ffffff;
    --backdrop: #ecebe7;
    --line-grey: #b9bcbf;
    --ghost-grey: #e2e3e4;
    --text-grey: #7d8287;
    --ink: #33383d;
  }
  html, body {
    margin: 0;
    width: 1200px;
    height: 778px;
    overflow: hidden;
    background: var(--backdrop);
    font-family: "Source Sans 3", Arial, sans-serif;
  }
  .stage { position: relative; width: 1200px; height: 778px; }
  .piece {
    position: absolute;
    background: var(--paper);
    overflow: hidden;
    box-shadow: 0 2px 6px rgba(0,0,0,.12);
  }
  .wordmark {
    font-family: "Montserrat", Arial, sans-serif;
    font-weight: 700;
    color: var(--brand-blue);
    letter-spacing: -0.01em;
    white-space: nowrap;
    line-height: 1;
  }
  .frame { position: absolute; inset: 0; width: 100%; height: 100%; }
  .frame path, .frame rect { fill: none; stroke: var(--line-grey); stroke-width: 1; }
  .footer-details {
    position: absolute;
    text-align: right;
    font-size: 9px;
    line-height: 1.45;
    color: var(--text-grey);
  }
  .side-ref {
    position: absolute;
    font-size: 7px;
    color: var(--text-grey);
    transform: rotate(-90deg);
    transform-origin: left top;
    letter-spacing: .05em;
  }

  /* Letterhead with large wordmark */
  .letterhead-feature { left: 0; top: 0; width: 715px; height: 372px; }
  .letterhead-feature .hero-mark {
    position: absolute; left: -6px; top: -26px; font-size: 210px;
  }
  .letterhead-feature .footer-details { right: 40px; bottom: 26px; }
  .letterhead-feature .side-ref { left: 30px; top: 250px; }

  /* Standard letterhead */
  .letterhead { left: 652px; top: 0; width: 540px; height: 372px; }
  .letterhead .header-mark { position: absolute; left: 22px; top: 40px; font-size: 19px; }
  .letterhead .date { position: absolute; right: 26px; top: 46px; font-size: 8px; color: var(--text-grey); }
  .letterhead .ghost-mark {
    position: absolute; left: 10px; top: 200px; font-size: 170px; color: var(--ghost-grey);
  }
  .letterhead .footer-details { right: 22px; bottom: 24px; }
  .letterhead .side-ref { left: 520px; top: 220px; }

  /* Envelope */
  .envelope { left: 14px; top: 398px; width: 812px; height: 288px; background: #f7f7f6; }
  .envelope .flap {
    position: absolute; left: 0; top: 0; width: 100%; height: 118px;
    background: var(--paper);
    box-shadow: 0 3px 5px rgba(0,0,0,.08);
  }
  .envelope .flap-mark { position: absolute; left: 2px; top: 2px; font-size: 118px; }

  /* Compliment slip */
  .comp-slip { left: 314px; top: 532px; width: 512px; height: 198px; z-index: 2; }
  .comp-slip .header-mark { position: absolute; left: 24px; top: 24px; font-size: 19px; }

  /* Business cards */
  .card {
    width: 282px; border-bottom: 7px solid var(--brand-blue);
    box-shadow: 0 3px 6px rgba(0,0,0,.14);
  }
  .card-front { left: 884px; top: 404px; height: 148px; display: flex; align-items: center; justify-content: center; }
  .card-front .card-mark { font-size: 27px; }
  .card-back { left: 884px; top: 580px; height: 158px; }
  .card-back .card-hero { position: absolute; left: -8px; top: -26px; font-size: 112px; }
  .card-back .holder { position: absolute; left: 26px; top: 96px; font-size: 10px; line-height: 1.35; color: var(--ink); }
  .card-back .holder-name { font-weight: 600; font-size: 11px; }
  .card-back .holder-contact { margin-top: 8px; color: var(--text-grey); font-size: 9px; }
  .card-back .card-web { position: absolute; right: 18px; bottom: 14px; font-size: 9px; color: var(--text-grey); }
</style>
</head>
<body>
<main class="stage">

  <section class="piece letterhead-feature" aria-label="Feature letterhead">
    <div class="wordmark hero-mark">BRIGHTHOLD</div>
    <svg class="frame" viewBox="0 0 715 372" aria-hidden="true">
      <path d="M22 230 V346 H440"/>
      <rect x="18" y="340" width="8" height="8"/>
    </svg>
    <span class="side-ref">REF 000 018</span>
    <div class="footer-details">Contact Consulting<br>www.brighthold.com<br>(001) 555 0142 | brighthold.com</div>
  </section>

  <section class="piece letterhead" aria-label="Letterhead">
    <div class="wordmark header-mark">BRIGHTHOLD</div>
    <div class="date">June 2018</div>
    <div class="wordmark ghost-mark">BRIGHT</div>
    <svg class="frame" viewBox="0 0 540 372" aria-hidden="true">
      <path d="M14 30 V20 H526 V30"/>
      <path d="M14 200 V352 H30"/>
      <path d="M510 352 H526 V200"/>
    </svg>
    <span class="side-ref">PAGE 01</span>
    <div class="footer-details">Contact Consulting<br>www.brighthold.com<br>(001) 555 0142 | brighthold.com</div>
  </section>

  <section class="piece envelope" aria-label="Envelope">
    <div class="flap">
      <div class="wordmark flap-mark">BRIGHTHOLD</div>
    </div>
  </section>

  <section class="piece comp-slip" aria-label="Compliment slip">
    <div class="wordmark header-mark">BRIGHTHOLD</div>
    <svg class="frame" viewBox="0 0 512 198" aria-hidden="true">
      <path d="M14 60 V184 H170"/>
      <path d="M14 14 H470"/>
      <rect x="482" y="10" width="8" height="8"/>
      <path d="M300 80 H470 L496 104 V184 H300 Z"/>
      <path d="M180 110 V184"/>
    </svg>
  </section>

  <section class="piece card card-front" aria-label="Business card front">
    <div class="wordmark card-mark">BRIGHTHOLD</div>
  </section>

  <section class="piece card card-back" aria-label="Business card back">
    <div class="wordmark card-hero">HOLD</div>
    <div class="holder">
      <div class="holder-name">Callum Fraser</div>
      <div class="holder-title">Chief Strategist</div>
      <div class="holder-contact">contact or contact info<br>we@brighthold.com</div>
    </div>
    <div class="card-web">brighthold.com</div>
  </section>

</main>
</body>
</html>
```